Stationary Design for Landscaping & Cleaning Business

Our landscaping and cleaning business need a stationary design, we would like separate designs for each business that match.
We want a simple yet bold design, using colours of our logos.
We are re designing our business so we need a more professional and modern look.
We don't want any extra words, just the basic contact details.
Name, address, phone number, email, abn and the usual customer details.
We would like to see examples for all stationary and both names.

Target Market(s)

No target market

Industry/Entity Type

Business

Font styles to use
Sans Serif

Colors
ffffff
000000

Requirements
Must have
• Business card, letterhead and envelope design.
Nice to have
• Lines and coloured areas
Should not have
• No extra pictures

```html
<!DOCTYPE html>
<html lang="en">
<head>
<meta charset="utf-8">
<title>Brightway Cleaning Stationery</title>
<link rel="stylesheet" href="https://fonts.googleapis.com/css2?family=Questrial&display=swap">
<style>
  :root {
    --purple: #9b1b8f;
    --black: #231f20;
    --paper: #fbfbfb;
    --ink: #555;
    --bg: #d6d6d6;
    --white: #ffffff;
  }
  * { box-sizing: border-box; margin: 0; padding: 0; }
  html, body { width: 1200px; height: 900px; overflow: hidden; }
  body {
    background: var(--bg);
    font-family: "Questrial", "Century Gothic", sans-serif;
    color: var(--ink);
    position: relative;
  }
  .sheet { position: absolute; background: var(--paper); overflow: hidden; box-shadow: 0 1px 3px rgba(0,0,0,.25); }
  .wave { position: absolute; left: 0; bottom: 0; width: 100%; display: block; }

  .brand { display: flex; align-items: center; gap: 4px; color: var(--purple); white-space: nowrap; letter-spacing: -0.2px; }
  .brand-dot { width: 6px; height: 6px; border-radius: 50%; background: var(--purple); flex: none; }
  .brand--light { color: var(--white); }
  .brand--light .brand-dot { background: var(--purple); }

  .contact-list { list-style: none; color: var(--ink); }
  .contact-list li { display: flex; align-items: center; gap: 3px; white-space: nowrap; }
  .icon { display: inline-block; background: var(--purple); flex: none; }

  /* Letterhead */
  .letterhead { left: 220px; top: 54px; width: 383px; height: 540px; }
  .letterhead .brand { position: absolute; left: 35px; top: 33px; font-size: 19px; }
  .letterhead .brand-dot { width: 7px; height: 7px; }
  .letterhead .contact { position: absolute; left: 282px; top: 33px; font-size: 5.6px; line-height: 7px; }
  .letterhead .contact .icon { width: 5px; height: 5px; }
  .letterhead .contact address { font-style: normal; margin-top: 5px; }
  .letter-body { position: absolute; left: 35px; top: 107px; width: 311px; font-size: 5.4px; line-height: 6.7px; }
  .letter-body .date { margin-bottom: 10px; }
  .letter-body .recipient { font-style: normal; margin-bottom: 30px; }
  .letter-body .salutation { font-weight: bold; margin-bottom: 8px; color: #333; }
  .letter-body p { margin-bottom: 6.5px; text-align: justify; }
  .signoff { display: flex; align-items: flex-start; gap: 8px; margin-top: 10px; }
  .signoff strong { color: #333; }
  .signature { width: 80px; height: 28px; background: linear-gradient(90deg, #e8ebf6, #d6dcf0); border-radius: 2px; }

  /* Presentation folder */
  .folder { position: absolute; left: 650px; top: 40px; width: 415px; height: 552px; background: var(--black); border-radius: 3px; box-shadow: 0 2px 5px rgba(0,0,0,.35); overflow: hidden; }
  .folder-spine { position: absolute; left: 23px; top: 0; bottom: 0; width: 2px; background: rgba(0,0,0,.45); }
  .folder .brand { position: absolute; left: 154px; top: 104px; font-size: 26px; }
  .folder .brand-dot { width: 9px; height: 9px; }

  /* Business cards */
  .card { width: 163px; height: 91px; }
  .card-front { left: 79px; top: 638px; }
  .card-front .brand { position: absolute; left: 10px; top: 42px; font-size: 8.5px; gap: 3px; }
  .card-front .brand-dot { width: 3.5px; height: 3.5px; }
  .card-front .person { position: absolute; left: 104px; top: 21px; width: 57px; font-size: 5px; line-height: 6px; }
  .person-name { color: var(--purple); font-weight: bold; letter-spacing: .3px; }
  .card-front .contact { margin-top: 4px; font-size: 3.9px; line-height: 5px; }
  .card-front .contact .icon { width: 3.5px; height: 3.5px; }
  .card-front .contact address { font-style: normal; margin-top: 3px; }
  .card-back { left: 79px; top: 748px; background: var(--black); }
  .card-back .brand { position: absolute; left: 14px; top: 40px; font-size: 10px; gap: 3px; }
  .card-back .brand-dot { width: 4px; height: 4px; }

  /* Envelopes */
  .envelope { width: 400px; height: 199px; }
  .envelope-front { left: 278px; top: 640px; }
  .envelope-front .brand { position: absolute; left: 20px; top: 27px; font-size: 19px; }
  .envelope-front .brand-dot { width: 7px; height: 7px; }
  .envelope-front address { position: absolute; left: 22px; top: 61px; font-style: normal; font-size: 5.6px; line-height: 7px; }
  .envelope-back { left: 724px; top: 640px; }
  .envelope-flap { position: absolute; left: 0; top: 0; width: 100%; height: 57px; display: block; }
  .flap-mark { position: absolute; left: 195px; top: 26px; width: 10px; height: 10px; border-radius: 50%; background: var(--purple); }
</style>
</head>
<body>

  <section class="sheet letterhead" aria-label="Letterhead">
    <div class="brand"><span class="brand-dot"></span>Brightway Cleaning</div>
    <div class="contact">
      <ul class="contact-list">
        <li><span class="icon"></span>08 9000 1234</li>
        <li><span class="icon"></span>hello@brightwaycleaning.au</li>
        <li><span class="icon"></span>www.brightwaycleaning.au</li>
      </ul>
      <address>12 Harbour Lane<br>Seaview WA 6000<br>ABN 00 000 000 000</address>
    </div>
    <div class="letter-body">
      <div class="date">30.02.2015</div>
      <address class="recipient">Recipient's name<br>Sample Street 1<br>10000 Berlin<br>Germany</address>
      <div class="salutation">Dear sir,</div>
      <p>Thank you for choosing our team for your home and office cleaning needs. This letter confirms the details of the service plan we discussed and the schedule agreed for the coming months. Please keep it with your records.</p>
      <p>Our staff will arrive at the agreed times with all equipment and supplies. Each visit includes floors, kitchens, bathrooms and common areas, finished to a consistent standard. Any extra tasks can be added with a short notice by phone or email before the visit.</p>
      <p>Invoices are issued at the end of each month and can be paid by bank transfer. Should you wish to change the plan, pause a visit or ask a question, our office is happy to help.</p>
      <p>We look forward to working with you and keeping your spaces clean, fresh and ready to use.</p>
      <div class="signoff">
        <div>Yours Sincerely,<br><strong>Lena Morris</strong></div>
        <div class="signature" role="img" aria-label="Handwritten signature of Lena Morris"></div>
      </div>
    </div>
    <svg class="wave" viewBox="0 0 383 30" height="30" preserveAspectRatio="none" aria-hidden="true">
      <path d="M0 12 C120 2 260 0 383 14 L383 30 L0 30 Z" fill="var(--purple)"/>
      <path d="M0 18 C120 10 250 8 383 18 L383 30 L0 30 Z" fill="#d9d9d9"/>
      <path d="M0 30 C110 16 260 12 383 21 L383 30 Z" fill="var(--black)"/>
    </svg>
  </section>

  <section class="folder" aria-label="Presentation folder">
    <div class="folder-spine"></div>
    <div class="brand brand--light"><span class="brand-dot"></span>Brightway Cleaning</div>
  </section>

  <section class="sheet card card-front" aria-label="Business card, front">
    <div class="brand"><span class="brand-dot"></span>Brightway Cleaning</div>
    <div class="person">
      <div class="person-name">SAM PORTER</div>
      <div>General Manager</div>
      <div class="contact">
        <ul class="contact-list">
          <li><span class="icon"></span>08 9000 1234</li>
          <li><span class="icon"></span>hello@brightwaycleaning.au</li>
          <li><span class="icon"></span>www.brightwaycleaning.au</li>
        </ul>
        <address>12 Harbour Lane<br>Seaview WA 6000<br>ABN 00 000 000 000</address>
      </div>
    </div>
    <svg class="wave" viewBox="0 0 163 14" height="14" preserveAspectRatio="none" aria-hidden="true">
      <path d="M0 7 C50 0 110 0 163 6 L163 14 L0 14 Z" fill="var(--purple)"/>
      <path d="M0 14 C45 5 110 4 163 9 L163 14 Z" fill="var(--black)"/>
    </svg>
  </section>

  <section class="sheet card card-back" aria-label="Business card, back">
    <div class="brand brand--light"><span class="brand-dot"></span>Brightway Cleaning</div>
  </section>

  <section class="sheet envelope envelope-front" aria-label="Envelope, front">
    <div class="brand"><span class="brand-dot"></span>Brightway Cleaning</div>
    <address>12 Harbour Lane<br>Seaview WA 6000</address>
    <svg class="wave" viewBox="0 0 400 28" height="28" preserveAspectRatio="none" aria-hidden="true">
      <path d="M0 10 C130 0 280 -2 400 10 L400 28 L0 28 Z" fill="var(--purple)"/>
      <path d="M0 17 C130 8 280 6 400 15 L400 28 L0 28 Z" fill="#d9d9d9"/>
      <path d="M0 28 C120 13 290 9 400 19 L400 28 Z" fill="var(--black)"/>
    </svg>
  </section>

  <section class="sheet envelope envelope-back" aria-label="Envelope, back">
    <svg class="envelope-flap" viewBox="0 0 400 57" preserveAspectRatio="none" aria-hidden="true">
      <path d="M0 0 L400 0 L388 57 L12 57 Z" fill="var(--black)"/>
    </svg>
    <span class="flap-mark"></span>
  </section>

</body>
</html>
```